TRK MECHANICAL FRONT WINDOWS DESIGN

I have two windows 2320 length, 1870 depth.
I would like a logo on one window, like the logo on sign we had designed with possibly the gears behind like in sign.
Other window would like same colours as logo with details of business.
The background colour I would maybe like the same as sign but if you think something looks better then happy to see design.
Details on other window:
ALL MECHANICAL REPAIRS, SERVICING AND MAJOR OVERHAULS ON LIGHT, HEAVY VEHICLES, DRILL RIGS, COMPRESSORS AND BOOSTERS
CERTIFIED VEHICLE REPAIRER
0451937264
tandkmechanical52@mailvane.net
Maybe just details in some sort of design or have a picture of a 46 SERIES dune strider, Brenk truck or an engine

```html
<!DOCTYPE html>
<html lang="en">
<head>
<meta charset="utf-8">
<title>TRK Mechanical – Front Windows</title>
<link rel="stylesheet" href="https://fonts.googleapis.com/css2?family=Russo+One&family=Saira:ital,wght@1,600&display=swap">
<style>
  :root {
    --backdrop: #58575a;
    --panel-dark: #0d0d0e;
    --panel-mid: #2e2e30;
    --ink: #2a2b2e;
    --ink-edge: #f3f3f3;
    --brand-blue: #1f86e6;
    --bronze: #6f6558;
  }
  * { margin: 0; padding: 0; box-sizing: border-box; }
  html, body {
    width: 1200px; height: 578px; overflow: hidden;
    background: var(--backdrop);
  }
  .canvas { position: relative; width: 1200px; height: 578px; }

  .window {
    position: absolute; top: 82px; width: 513px; height: 413px;
    box-shadow: 4px 5px 7px rgba(0,0,0,.45);
    overflow: hidden;
  }

  /* Logo window */
  .window--logo {
    left: 61px;
    background: radial-gradient(ellipse at 50% 45%, var(--panel-mid) 0%, var(--panel-dark) 75%);
  }
  .gear-art {
    position: absolute; left: 51px; top: 33px; width: 410px; height: 356px;
    border-radius: 46%;
    background: radial-gradient(circle at 50% 50%, #9c9da0 0%, #6a6b6e 45%, rgba(60,60,63,.6) 70%, rgba(20,20,22,0) 100%);
  }
  .brand-name {
    position: absolute; left: 0; right: 0; top: 192px;
    text-align: center;
    font-family: "Russo One", sans-serif;
    font-size: 40px; line-height: 1; font-weight: 400;
    color: var(--brand-blue);
    letter-spacing: 1px;
  }

  /* Details window */
  .window--details {
    left: 626px;
    background: linear-gradient(180deg,
      #f4f4f5 0px, #d9d9db 22px, #7e7f82 30px,
      #b9babd 60px, #9c9da0 120px, #c4c5c7 150px,
      #5d5c5a 165px, var(--bronze) 195px, #a29a8f 230px, #4a4845 255px,
      #3c3c3e 262px, #d6d6d8 285px, #a5a6a9 310px, #555659 318px,
      #c9cacc 340px, #8e8f92 413px);
  }
  .ink-text {
    font-family: "Russo One", sans-serif;
    color: var(--ink);
    text-shadow: 1px 1px 0 var(--ink-edge);
    line-height: 1;
    white-space: nowrap;
  }
  .services {
    position: absolute; left: 0; right: 0; top: 42px;
    text-align: center;
    font-style: italic;
    font-size: 22.5px; line-height: 28px;
    text-transform: uppercase;
  }
  .certified__seal { position: absolute; left: 85px; top: 172px; width: 72px; height: 72px; }
  .certified__title {
    position: absolute; left: 166px; top: 175px;
    font-size: 47px;
  }
  .certified__sub {
    position: absolute; left: 167px; top: 218px;
    font-style: italic;
    font-size: 24px;
  }
  .phone__icon { position: absolute; left: 92px; top: 266px; width: 26px; height: 38px; }
  .phone__number {
    position: absolute; left: 124px; top: 265px;
    font-style: italic;
    font-size: 41px; letter-spacing: 2px;
  }
  .swoosh { position: absolute; left: 0; top: 320px; width: 513px; height: 93px; }
  .email__icon { position: absolute; left: 16px; top: 375px; width: 36px; height: 26px; }
  .email__address {
    position: absolute; left: 60px; top: 375px;
    font-family: "Saira", sans-serif;
    font-style: italic; font-weight: 600;
    font-size: 21px;
  }
</style>
</head>
<body>
<main class="canvas">

  <section class="window window--logo">
    <div class="gear-art" role="img" aria-label="Interlocking steel gears and pulleys arranged behind the business name"></div>
    <h1 class="brand-name">TRK MECHANICAL</h1>
  </section>

  <section class="window window--details">
    <p class="services ink-text">
      All mechanical repairs,<br>
      servicing and major overhauls<br>
      on light, heavy vehicles, drill rigs,<br>
      compressors and boosters
    </p>

    <svg class="certified__seal" viewBox="0 0 74 74" aria-hidden="true">
      <circle cx="37" cy="37" r="35" fill="var(--ink)" stroke="var(--ink-edge)" stroke-width="1.5"/>
      <circle cx="37" cy="37" r="26" fill="none" stroke="var(--ink-edge)" stroke-width="3"/>
      <path d="M25 38 L34 47 L50 28" fill="none" stroke="var(--ink-edge)" stroke-width="5" stroke-linecap="round" stroke-linejoin="round"/>
    </svg>
    <span class="certified__title ink-text">CERTIFIED</span>
    <span class="certified__sub ink-text">VEHICLE REPAIRER</span>

    <svg class="phone__icon" viewBox="0 0 28 38" aria-hidden="true">
      <path d="M7 2 L12 2 L13 10 L9 13 Q10 22 16 28 L20 25 L26 29 L25 35 Q21 37 17 35 Q5 26 3 10 Q3 4 7 2 Z" fill="var(--ink)"/>
    </svg>
    <span class="phone__number ink-text">0451937264</span>

    <svg class="swoosh" viewBox="0 0 513 93" preserveAspectRatio="none" aria-hidden="true">
      <defs>
        <linearGradient id="swoosh-fill" x1="0" y1="0" x2="1" y2="0">
          <stop offset="0" stop-color="#b9babd"/>
          <stop offset=".5" stop-color="#e4e5e6"/>
          <stop offset="1" stop-color="#8d8e91"/>
        </linearGradient>
      </defs>
      <path d="M0 30 Q210 -8 513 82 L513 93 L0 93 Z" fill="url(#swoosh-fill)"/>
      <path d="M0 22 Q210 -14 513 74" fill="none" stroke="#f7f7f7" stroke-width="4"/>
      <path d="M0 30 Q210 -8 513 82" fill="none" stroke="var(--ink)" stroke-width="3"/>
    </svg>

    <svg class="email__icon" viewBox="0 0 36 26" aria-hidden="true">
      <rect x="1" y="1" width="34" height="24" rx="2" fill="var(--ink)"/>
      <path d="M3 3 L18 15 L33 3" fill="none" stroke="var(--ink-edge)" stroke-width="2.5"/>
    </svg>
    <span class="email__address ink-text">tandkmechanical52@mailvane.net</span>
  </section>

</main>
</body>
</html>
```